Take out menu for The Lantern Nook Café

I'd like to have my menu re imagined.
Menu: (see LanternNookCafe Current menu file)
- Using the "new menu" and "cater menu" files which are updated over the LanternNookCafe Current menu
- Should be able to fit onto 11 x 17 parallel fold design
- Similar to current menu with headings and menu descriptions
- I do not have a font preference, whatever you think looks great and is easily readable
- More creative layout
- No pics of real foods
- Keeping the colors in "Salad, Grill, Sandwich, etc"
- The Cover page needs to be more of a cover, with all the same information, just more creative layout using the new logo attached.
- Do not need the "Harborline Roasters" and "Bellavita" logos that are on the current menu..
- With the background colors I'd like to stay with either bright type of green to signify "fresh", bright yellow, sky blue and/or white.
- The ** menu items should be featured
- "LanternNookCafe Current Menu" cover has all the pertinent information that I would also like on the new menu. Front cover should include: Logo, address, phone, fax, email, hours, "Catering Trays Always Avaialable" "Visit thelanternnookcafe.com to see our weekly specials!" "Dine In, Take Out or Delivery" Facebook, Twitter, Instagram logos.
The above mentioned for the front cover do not need to be in that particular order.
- Prefer the logo to be over a white background always
- Back cover should have somewhere, maps shot (LNMap), "Free Parking" "Free Wireless" "Delivery Minimum $10"
- With the maps shot on back, please insert the logo where it currently says "The Lantern Nook Cafe"
The Lantern Nook Cafe is a breakfast and lunch cafe serving mostly corporate clientele. As the owner, I am laid back and whimsical and I'd like that to reflect in the designs. Nothing fancy or serious, that's not my intention with the design.
thelanternnookcafe.com
Any questions please ask. Thank you in advance to all the talented designers for working on my project, it is greatly appreciated!

```html
<!DOCTYPE html>
<html lang="en">
<head>
<meta charset="utf-8">
<title>The Lantern Nook Café — Menu</title>
<link href="https://fonts.googleapis.com/css2?family=Gochi+Hand&family=Open+Sans:wght@400;600;700&family=Cabin+Sketch:wght@700&display=swap" rel="stylesheet">
<style>
:root{
  --paper:#f1ebc6;
  --paper-dark:#e6dcae;
  --garden:#1f9a3c;
  --grill:#d3222a;
  --sandwich:#2a84c6;
  --breakfast:#f05a28;
  --ink:#5a5a55;
  --dark:#1d1d1b;
  --note:#c9da8f;
  --grass:#a9c35a;
}
*{margin:0;padding:0;box-sizing:border-box}
html,body{width:1200px;height:776px;overflow:hidden}
body{
  position:relative;
  background:radial-gradient(ellipse at 50% 40%,#f5f0d2 0%,var(--paper) 55%,var(--paper-dark) 100%);
  font-family:'Open Sans',Arial,sans-serif;
  color:var(--ink);
}
.column{position:absolute;top:18px}
.col-garden{left:18px;width:272px}
.col-grill{left:322px;width:272px}
.col-sandwich{left:618px;width:272px}
.col-right{left:914px;width:280px}

.section-title{
  display:inline-block;
  font-family:'Cabin Sketch',cursive;
  font-size:27px;letter-spacing:1px;line-height:1;
  background:#fff;padding:3px 6px 2px;
  box-shadow:2px 2px 0 rgba(255,255,255,.7),-2px -1px 0 rgba(255,255,255,.6);
}
.garden .section-title{color:var(--garden)}
.grill .section-title{color:var(--grill)}
.sandwich .section-title{color:var(--sandwich)}
.breakfast .section-title{color:var(--breakfast)}
.soup .section-title,.combos .section-title{color:var(--grill)}

.instructions{
  margin:14px 0 18px;
  border:1px solid var(--dark);
  padding:2px 6px;
  font-family:'Gochi Hand',cursive;font-size:10.5px;line-height:1.2;color:var(--dark);
}
.item{margin-bottom:13px}
.item h3{font-size:9.3px;font-weight:700;line-height:1.15;text-transform:uppercase}
.item p{font-size:7.6px;line-height:1.32}
.garden .item h3{color:var(--garden)}
.grill .item h3{color:var(--grill)}
.sandwich .item h3{color:var(--sandwich)}
.breakfast .item h3{color:var(--breakfast)}
.grill .item{margin-bottom:15.5px}
.sandwich .item{margin-bottom:14.5px}

.note{
  position:absolute;background:var(--note);
  font-family:'Gochi Hand',cursive;color:var(--dark);
  font-size:10.5px;line-height:1.4;
}
.note-garden{left:8px;top:630px;width:288px;padding:8px 10px}
.note-sandwich{left:608px;top:656px;width:282px;padding:9px 10px;text-align:center}

.combos{position:relative;border:3px solid var(--dark);padding:4px 8px 6px;height:128px}
.combos ul{list-style:none;font-family:'Gochi Hand',cursive;font-size:10.5px;line-height:1.2;color:var(--dark);margin-top:6px}
.stamp{position:absolute;right:10px;top:14px}
.soup{margin-top:8px}
.soup p{color:var(--breakfast);font-size:8.5px;font-weight:700;line-height:1.3;margin-top:12px}
.breakfast{margin-top:14px}
.breakfast .section-title{margin-bottom:12px}
.breakfast .item{margin-bottom:12.5px}
.fine{position:absolute;right:12px;top:712px;font-size:7.5px;color:var(--ink)}
.grass{position:absolute;left:0;bottom:0;width:1200px;height:62px;
  background:linear-gradient(180deg,rgba(169,195,90,0) 0%,rgba(169,195,90,.55) 45%,var(--grass) 100%)}
</style>
</head>
<body>

<section class="column col-garden garden">
  <h2 class="section-title">GARDEN</h2>
  <p class="instructions">Choose Either On A Bed Of Greens Or In A Wheat, White, Spinach, Or Tomato Wrap, Served Cold</p>
  <div class="item"><h3>Caesar</h3><p>Romaine lettuce, diced chicken, parmesan cheese and creamy Caesar dressing. Salad 6.50; Wrap 5.95</p></div>
  <div class="item"><h3>Buffalo</h3><p>Romaine lettuce, diced chicken spiked with hot sauce, celery, bleu cheese crumbles and ranch dressing. Salad 6.50; Wrap 5.95</p></div>
  <div class="item"><h3>Turkey</h3><p>Romaine lettuce, home cooked all natural turkey, bacon, tomatoes, mixed cheese and ranch dressing. Salad 6.50; Wrap 5.95</p></div>
  <div class="item"><h3>Chef's</h3><p>Romaine lettuce, home cooked all natural turkey, tavern ham, mixed cheese, egg, bacon, tomatoes, red onions, cucumbers and thousand island dressing. Salad 6.75; Wrap 6.25</p></div>
  <div class="item"><h3>Cali Cobb</h3><p>Romaine lettuce, diced chicken, avocado, tomatoes, bacon, egg, bleu cheese crumbles and zesty avocado ranch. Salad 6.75; Wrap 6.25</p></div>
  <div class="item"><h3>Greek</h3><p>Spinach, diced chicken, black olives, tomatoes, red onions, cucumber, feta cheese and balsamic vinaigrette dressing. Salad 6.75; Wrap 6.25</p></div>
  <div class="item"><h3>Asian Sesame</h3><p>Romaine lettuce, diced chicken, mandarin oranges, sliced almonds, carrots, sesame seeds, crunchy Asian noodles and Asian sesame dressing. Salad 6.75; Wrap 6.25</p></div>
  <div class="item"><h3>Apple Walnut</h3><p>Romaine lettuce, diced chicken, tomatoes, craisins, apple chips, crumbled bleu cheese, walnuts and ranch dressing. Salad 6.75; Wrap 6.25</p></div>
  <div class="item"><h3>Tomato, Mozzarella &amp; Spinach</h3><p>Spinach, tomatoes, cucumbers, sauteed onions, fresh mozzarella and olive oil with balsamic vinaigrette. Salad 6.75; Wrap 6.25</p></div>
  <div class="item"><h3>Salad Salad</h3><p>Romaine lettuce and either chicken, egg or tuna salad (or all 3), tomatoes, carrots and red onions. Salad 6.75; Wrap 6.25</p></div>
</section>
<p class="note note-garden">Can remove meats from any of the above 1.00 less<br>Dressings: Bleu Cheese, Honey Mustard, Thousand Island, Creamy Caesar, Asian Sesame, Balsamic Vinaigrette, Fat Free Raspberry Vinaigrette, Olive Oil Vinaigrette, Ranch, Avocado Ranch, Lite Golden Italian, Creamy Italian, French</p>

<section class="column col-grill grill">
  <h2 class="section-title">GRILL</h2>
  <p class="instructions">Choose from a kaiser roll, sourdough, marble rye, pita or wrap, served hot</p>
  <div class="item"><h3>Barbecue Chicken</h3><p>Seasoned chicken, bbq sauce, red onions, bacon and cheddar cheese, served with ranch dressing. 6.25</p></div>
  <div class="item"><h3>Fajita</h3><p>Seasoned chicken, peppers, onions, mixed cheese and side salsa and sour cream. 6.25</p></div>
  <div class="item"><h3>Chicken Mozz</h3><p>Seasoned chicken, tomatoes, spinach, fresh mozzarella and balsamic vinaigrette. 6.25</p></div>
  <div class="item"><h3>Reuben / Rachel</h3><p>Choose from: home cooked all natural turkey, home cooked toast beef or tavern ham, with kraut or coleslaw, Swiss and thousand island. 6.25</p></div>
  <div class="item"><h3>Veggie</h3><p>Fresh mozzarella cheese, spinach, tomato, cucumber, red onions, roasted red peppers and balsamic vinaigrette. 6.25</p></div>
  <div class="item"><h3>Commerce</h3><p>Seasoned chicken, provolone, spinach, bacon and ranch. 6.25</p></div>
  <div class="item"><h3>Cajun Chicken</h3><p>Chicken with cajun seasoning, provolone or pepper jack cheese, onions, tomato and ranch. 6.25</p></div>
  <div class="item"><h3>Cordon Bleu</h3><p>Seasoned chicken, tavern ham, Swiss and honey mustard. 6.25</p></div>
  <div class="item"><h3>Chipotle Ranch Turkey</h3><p>Homemade turkey, bacon, red onion, pepper jack cheese and chipotle ranch sauce. 6.50</p></div>
  <div class="item"><h3>Roast Beef and Bleu</h3><p>Homemade roast beef, onions, crumbled bleu cheese and spicy horseradish sauce. 6.50</p></div>
  <div class="item"><h3>Tuna Melt</h3><p>Homemade tuna salad, tomatoes and Swiss. 6.50</p></div>
  <div class="item"><h3>Mediterranean</h3><p>Seasoned chicken, fresh mozzarella, roasted red peppers and spinach. 6.50</p></div>
  <div class="item"><h3>Crazy Cheese</h3><p>Cheddar, American, Swiss, and tomato. 4.25 Add bacon 1.00</p></div>
</section>

<section class="column col-sandwich sandwich">
  <h2 class="section-title">SANDWICHES</h2>
  <p class="instructions">Choose from a kaiser, hoagie, sourdough, marble rye, pita, wrap, white or wheat toast</p>
  <div class="item"><h3>B.L.T.</h3><p>A true classic with bacon, lettuce, tomato and mayo. 5.25</p></div>
  <div class="item"><h3>Turkey Club</h3><p>A triple decker! Home cooked all natural turkey, tomato, bacon, lettuce, Swiss and mayo. 6.50</p></div>
  <div class="item"><h3>Junkyard</h3><p>Homemade roast beef, all natural turkey, tavern ham, pepperoni, lettuce, tomato, Swiss and mayo. 6.50</p></div>
  <div class="item"><h3>Roast Beef</h3><p>Homemade roast beef, lettuce, tomato, provolone and spicy horseradish sauce. 6.50</p></div>
  <div class="item"><h3>Tuna Salad</h3><p>Homemade all white tuna, with lettuce and tomato. 6.50<br>Add cheese .25</p></div>
  <div class="item"><h3>Veggie Avocado</h3><p>Avocado, roasted peppers, cucumber, red onions, Swiss cheese, lettuce, tomato and avocado ranch. 6.50</p></div>
  <div class="item"><h3>Turkey Bacon Ranch</h3><p>Home cooked turkey, bacon, cheddar cheese, tomato and ranch. 6.50</p></div>
  <div class="item"><h3>Italian</h3><p>Cappicola, salami, pepperoni, provolone, lettuce, tomato and onion. 6.50</p></div>
  <div class="item"><h3>Chicken Salad</h3><p>Homemade with celery and spices, with lettuce and tomato. 6.25<br>Add cheese .50</p></div>
  <div class="item"><h3>Ham and Swiss</h3><p>Sliced tavern ham and Swiss with lettuce, tomato, mayo and mustard. 5.95</p></div>
  <div class="item"><h3>Egg Salad</h3><p>Homemade with spices, lettuce and tomato. 5.95 Add cheese .50</p></div>
  <div class="item"><h3>PBBE-J</h3><p>Peanut butter or Hazelnutty spread and jelly with bananas and lightly grilled. 4.95</p></div>
</section>
<p class="note note-sandwich">If you don't see what you want on the menu,<br>we will try and make it for you!</p>

<aside class="column col-right">
  <section class="combos">
    <h2 class="section-title">COMBOS</h2>
    <ul>
      <li>Choose two, 6.50</li>
      <li>+ 1/2 Sandwich</li>
      <li>+ 1/2 Salad</li>
      <li>+ Soup</li>
      <li>+ Quiche</li>
    </ul>
    <svg class="stamp" width="92" height="92" viewBox="0 0 92 92" aria-label="Try our favourite together!">
      <circle cx="46" cy="46" r="40" fill="none" stroke="#1d1d1b" stroke-width="4"/>
      <g font-family="Gochi Hand, cursive" font-size="11" fill="#1d1d1b" text-anchor="middle" transform="rotate(18 46 46)">
        <text x="46" y="33">Try our</text>
        <text x="46" y="48">favourite</text>
        <text x="46" y="63">together!</text>
      </g>
    </svg>
  </section>

  <section class="soup">
    <h2 class="section-title">SOUP</h2>
    <p>8 oz. - 3.15<br>12 oz. - 3.50</p>
  </section>

  <section class="breakfast">
    <h2 class="section-title">BREAKFAST</h2>
    <div class="item"><h3>Breakfast Sandwich</h3><p>Two eggs and American cheese on; bagel, English muffin or croissant with choice of meat. 3.75</p></div>
    <div class="item"><h3>Eggs Your Way</h3><p>Two eggs cooked to order with meat and toast. 3.75</p></div>
    <div class="item"><h3>Omelet</h3><p>Three eggs with your choice of up to 3 fillings and toast. 4.25</p></div>
    <div class="item"><h3>Burrito</h3><p>Two eggs, meat, mixed cheese, onions, peppers and salsa. 4.25</p></div>
    <div class="item"><h3>Cheesesteak Breakfast Wrap</h3><p>Two eggs, cheesesteak, onions and American cheese 4.25</p></div>
    <div class="item"><h3>Greek Pita</h3><p>Two eggs, spinach and feta. 4.50</p></div>
    <div class="item"><h3>Avocado Egg Croissant</h3><p>Two eggs, avocado spread and cheddar cheese. 4.50</p></div>
    <div class="item"><h3>French Toast</h3><p>Two thick slices of brioche with choice of meat. 4.25</p></div>
    <div class="item"><h3>Quiche du Jour 3.75</h3></div>
    <div class="item"><h3>Bagel</h3><p>With cream cheese. 2.15</p></div>
    <div class="item"><h3>English Muffin, Croissant or Muffin 1.55<br>2 Pieces of Buttered Toast 1.00</h3><p>Side meat: bacon, sausage, ham, turkey sausage, pork roll 1.00<br>Side hash browns. 1.50</p></div>
  </section>
</aside>
<p class="fine">Prices subject to change...</p>

<div class="grass" role="img" aria-label="Illustrated strip of green grass along the bottom edge"></div>
</body>
</html>
```